Sanding Disc Box Packaging Graphic design

We need a package design for 5" hook and loop sanding discs designed for use with random orbital sanders.

The Brand name is "BADGER BITE". Our brand stands for Quality, Strength and durability at an affordable price.
Sanding discs packaging, and tool packaging tends to be very functional and straightforward. We are looking for a package design that is creative and stands out while maintaining a serious and professional quality look. Identifying closely with our brand name is very important as well.

I've attached images of the product, and the image the branding was inspired from. A color palette based on those images would be nice but is not necessarily required. Please note however that our discs are yellow and not red.

We do not have our box template from our manufacturer yet but the dimensions of the box will be 127x127x74mm

Target Market(s)

We are aiming at a beginner to mid-level power tool user.

Industry/Entity Type

Power Tool

Font styles to use
Serif
Decorative

Colors

Designer to choose colors to be used in the design.

Requirements
Must have
• Our Brand name, Badger Bite must be on the box, preferably in a strong Bold font.
• We would also like our slogan somewhere on the box: "Designed for Strength, Built to Last"
• I've also attached an image showing the number of pieces of each grit sandpaper is in each box. We would like some similar indication on our packaging. Also an indication that these are 8 hole sanding discs is needed as well.
Nice to have
• The packaging may also be used for other sanding products such as sanding belts, sponges, etc as the line expands so versatility is a plus. A vector design is preferred.
• A space on the back of the package for a more detailed product description with a matching font would helpful. The copy hasn't been written yet but the description will around 100 words. Placeholder text would be fine.
Should not have
• Absolutely DO NOT use images from other artists within your design. If this is done you will not win this design contest. I
• Also, please do not use the attached gorilla image in your designs. We have tried to locate the copyright holder to obtain printing rights but haven't been successful.
• Also, please stay away from the aesthetic of the product "Walrus paste". For trademark purposes the design needs to be as distinct from that product logo and packaging as possible.

```html
<!DOCTYPE html>
<html lang="en">
<head>
<meta charset="utf-8">
<title>Badger Bite – Sanding Disc Box Panels</title>
<link rel="stylesheet" href="https://fonts.googleapis.com/css2?family=Bebas+Neue&family=Oswald:wght@400;500&display=swap">
<style>
  :root {
    --bg: #e4e4e4;
    --box-black: #0e0e0e;
    --box-yellow: #f4e56e;
    --olive: #b9ad3c;
    --olive-light: #d8cc55;
    --gray: #d2d2d2;
    --white: #f2f2f2;
  }
  html, body {
    margin: 0; padding: 0;
    width: 1200px; height: 1000px;
    overflow: hidden;
    background: var(--bg);
  }
  .canvas { position: relative; width: 1200px; height: 1000px; }

  .panel { position: absolute; box-sizing: border-box; overflow: hidden; }

  /* Top lid */
  .panel-top {
    left: 147px; top: 57px; width: 560px; height: 326px;
    background: var(--box-yellow);
    display: flex; align-items: center; justify-content: center;
  }
  .brand-name {
    font-family: "Bebas Neue", sans-serif;
    font-weight: 400;
    color: var(--box-black);
    font-size: 96px; line-height: 0.9;
    text-align: center; margin: 0;
  }

  /* Front face */
  .panel-front {
    left: 147px; top: 383px; width: 560px; height: 560px;
    background: var(--box-black);
  }
  .front-art {
    position: absolute; left: 40px; top: 130px; width: 230px; height: 320px;
    border-radius: 40% 40% 35% 35%;
    background: radial-gradient(ellipse at 50% 40%, #cfcfcf 0%, #8c8c8c 55%, #2a2a2a 100%);
  }
  .front-title {
    position: absolute; right: 30px; top: 30px; margin: 0;
    text-align: right;
    font-family: "Bebas Neue", sans-serif;
    font-weight: 400;
    line-height: 0.86;
    white-space: nowrap;
  }
  .front-title .word-one { display: block; font-size: 88px; color: var(--olive); }
  .front-title .word-two { display: block; font-size: 170px; color: var(--olive); }
  .slogan { display: block; color: var(--gray); }
  .slogan-designed { font-size: 76px; }
  .slogan-strength { font-size: 52px; }
  .slogan-last { font-size: 54px; color: var(--white); }

  .disc-row {
    position: absolute; right: 30px; bottom: 30px;
    display: flex; gap: 16px;
  }
  .disc { width: 52px; height: 52px; }

  /* Side face */
  .panel-side {
    left: 707px; top: 383px; width: 326px; height: 560px;
    background: var(--box-black);
    border-left: 1px solid #222;
  }
  .side-heading {
    position: absolute; left: 18px; top: 22px; margin: 0;
    font-family: "Oswald", sans-serif; font-weight: 500;
    font-size: 20px; line-height: 1.2; color: var(--olive-light);
    white-space: nowrap;
  }
  .side-copy {
    position: absolute; left: 18px; top: 72px; width: 196px; margin: 0;
    font-family: "Oswald", sans-serif; font-weight: 400;
    font-size: 8.6px; line-height: 1.32; text-transform: uppercase;
    color: var(--white);
  }
  .grit-list {
    position: absolute; right: 18px; top: 68px; margin: 0; padding: 0;
    list-style: none; text-align: center;
    font-family: "Bebas Neue", sans-serif; color: var(--gray);
  }
  .grit-item { margin-bottom: 12px; line-height: 0.9; }
  .grit-count, .grit-label { display: block; font-size: 30px; }
  .grit-size { display: block; font-size: 50px; color: var(--white); }
  .side-art {
    position: absolute; left: 14px; top: 392px; width: 206px; height: 140px;
    border-radius: 45% 45% 20% 20%;
    background: radial-gradient(ellipse at 55% 45%, #c9bd4a 0%, #7d7428 60%, #1a1a1a 100%);
  }
  .disc-size {
    position: absolute; right: 24px; bottom: 16px; margin: 0;
    font-family: "Bebas Neue", sans-serif; font-size: 60px; line-height: 1;
    color: var(--white);
  }
</style>
</head>
<body>
<div class="canvas">

  <section class="panel panel-top">
    <h1 class="brand-name">Badger<br>Bite</h1>
  </section>

  <section class="panel panel-front">
    <div class="front-art" role="img" aria-label="Illustration of a roaring badger head in grey with yellow eyes"></div>
    <h2 class="front-title">
      <span class="word-one">BADGER</span>
      <span class="word-two">BITE</span>
      <span class="slogan slogan-designed">DESIGNED</span>
      <span class="slogan slogan-strength">FOR STRENGTH</span>
      <span class="slogan slogan-last">BUILT TO LAST</span>
    </h2>
    <div class="disc-row" aria-label="8 hole sanding discs">
      <svg class="disc" viewBox="0 0 52 52"><circle cx="26" cy="26" r="26" fill="#b9ad3c"/><g fill="#0e0e0e"><circle cx="26" cy="26" r="2"/><circle cx="26" cy="12" r="2"/><circle cx="26" cy="40" r="2"/><circle cx="12" cy="26" r="2"/><circle cx="40" cy="26" r="2"/><circle cx="16" cy="16" r="2"/><circle cx="36" cy="16" r="2"/><circle cx="16" cy="36" r="2"/><circle cx="36" cy="36" r="2"/></g></svg>
      <svg class="disc" viewBox="0 0 52 52"><circle cx="26" cy="26" r="26" fill="#b9ad3c"/><g fill="#0e0e0e"><circle cx="26" cy="26" r="2"/><circle cx="26" cy="12" r="2"/><circle cx="26" cy="40" r="2"/><circle cx="12" cy="26" r="2"/><circle cx="40" cy="26" r="2"/><circle cx="16" cy="16" r="2"/><circle cx="36" cy="16" r="2"/><circle cx="16" cy="36" r="2"/><circle cx="36" cy="36" r="2"/></g></svg>
      <svg class="disc" viewBox="0 0 52 52"><circle cx="26" cy="26" r="26" fill="#b9ad3c"/><g fill="#0e0e0e"><circle cx="26" cy="26" r="2"/><circle cx="26" cy="12" r="2"/><circle cx="26" cy="40" r="2"/><circle cx="12" cy="26" r="2"/><circle cx="40" cy="26" r="2"/><circle cx="16" cy="16" r="2"/><circle cx="36" cy="16" r="2"/><circle cx="16" cy="36" r="2"/><circle cx="36" cy="36" r="2"/></g></svg>
      <svg class="disc" viewBox="0 0 52 52"><circle cx="26" cy="26" r="26" fill="#b9ad3c"/><g fill="#0e0e0e"><circle cx="26" cy="26" r="2"/><circle cx="26" cy="12" r="2"/><circle cx="26" cy="40" r="2"/><circle cx="12" cy="26" r="2"/><circle cx="40" cy="26" r="2"/><circle cx="16" cy="16" r="2"/><circle cx="36" cy="16" r="2"/><circle cx="16" cy="36" r="2"/><circle cx="36" cy="36" r="2"/></g></svg>
    </div>
  </section>

  <section class="panel panel-side">
    <h3 class="side-heading">HOOK AND LOOP SANDING DISCS</h3>
    <p class="side-copy">Lorem ipsum dolor sit amet, consectetur adipiscing elit, sed do eiusmod tempor incididunt ut labore et dolore magna aliqua. Ut enim ad minim veniam, quis nostrud exercitation ullamco laboris nisi ut aliquip ex ea commodo consequat. Duis aute irure dolor in reprehenderit in voluptate velit esse cillum dolore eu fugiat nulla pariatur. Excepteur sint occaecat cupidatat non proident, sunt in culpa qui officia deserunt mollit anim id est laborum. Lorem ipsum dolor sit amet, consectetur adipiscing elit, sed do eiusmod tempor incididunt ut labore et dolore magna aliqua. Ut enim ad minim veniam, quis nostrud exercitation ullamco laboris nisi ut aliquip ex ea commodo consequat. Duis aute irure dolor in reprehenderit in voluptate velit esse cillum dolore eu fugiat nulla pariatur. Excepteur sint occaecat cupidatat non proident, sunt in culpa qui officia deserunt mollit anim id est laborum.</p>
    <ul class="grit-list">
      <li class="grit-item"><span class="grit-count">20X</span><span class="grit-size">80</span><span class="grit-label">GRIT</span></li>
      <li class="grit-item"><span class="grit-count">20X</span><span class="grit-size">120</span><span class="grit-label">GRIT</span></li>
      <li class="grit-item"><span class="grit-count">20X</span><span class="grit-size">220</span><span class="grit-label">GRIT</span></li>
    </ul>
    <div class="side-art" role="img" aria-label="Illustration of a crouching, roaring badger in yellow and grey"></div>
    <p class="disc-size">5”</p>
  </section>

</div>
</body>
</html>
```